Geschäftspapiere für Rechtsanwaltskanzlei
Zielgruppe
Rechtsanwaltskanzlei mit dem Spezialgebiet Urheber-/Medienrecht; Mandanten sind Urheber, insbesondere von Musik- und Filmwerken, sowie Unternehmen, deren Unternehmenszweck die Herstellung- und Verwertung vorstehender Werke ist (z.B. Verlage, Filmproduktionsunternehmen). Das Design soll seriös sein, dabei aber einen modernen Touch haben.
Aufgabenstellung
Das Design muss im schwarz-weiß Ausdruck gut lesbar sein.
Es sollen folgende Informationen enthalten sein
Rechtsanwaltskanzlei Brunsmann
Rechtsanwältin Helga Brunsmann, MBA
Wiesenhang 27
14059 Berlin
Helga.Brunsmann@ra-brunsmann.com
Tel: +491524718260

```html
<!DOCTYPE html>
<html lang="de">
<head>
<meta charset="utf-8">
<title>Briefbogen Rechtsanwaltskanzlei Brunsmann</title>
<link href="https://fonts.googleapis.com/css2?family=Jost:wght@300;400;600&display=swap" rel="stylesheet">
<style>
  :root {
    --wine: #5a1214;
    --taupe: #786857;
    --ink: #222222;
    --rule: #8a8a8a;
    --paper: #ffffff;
  }
  * { margin: 0; padding: 0; box-sizing: border-box; }
  html, body { width: 863px; height: 1200px; overflow: hidden; background: var(--paper); }
  body { position: relative; font-family: 'Jost', sans-serif; color: var(--ink); font-weight: 400; }
  .sheet { position: absolute; left: 38px; top: 43px; width: 787px; height: 1114px; border: 1px solid var(--rule); }
  .band { position: absolute; left: 0; width: 863px; height: 15px; }
  .band-top { top: 43px; }
  .band-bottom { top: 1142px; }
  .abs { position: absolute; white-space: nowrap; }

  .brand-name { left: 589px; top: 106px; font-size: 37px; font-weight: 300; color: var(--wine); letter-spacing: 0.5px; line-height: 1; }
  .brand-sub { left: 590px; top: 162px; font-size: 15px; font-weight: 400; letter-spacing: 2.1px; color: var(--ink); line-height: 1; }

  .return-line { left: 120px; top: 220px; width: 300px; border-bottom: 1px solid var(--ink); font-size: 8.4px; text-align: center; padding-bottom: 3px; padding-left: 8px; }
  .return-line .sep { margin: 0 5px; }

  .contact { left: 581px; top: 259px; height: 103px; border-left: 1px solid var(--ink); padding-left: 9px; font-size: 12px; line-height: 16px; }
  .contact p { margin: 0; }
  .contact .gap { margin-top: 9px; }

  .dot { position: absolute; width: 1px; height: 1px; background: var(--ink); top: 388px; }

  .field { top: 415px; font-size: 11.8px; }

  .fold { position: absolute; left: 38px; width: 14px; height: 1px; background: var(--taupe); }

  .footer-col { top: 1090px; height: 43px; border-left: 1px solid var(--ink); padding-left: 8px; font-size: 9.8px; line-height: 13px; }
  .footer-col strong { color: var(--wine); font-weight: 600; }
  .footer-brand .name { font-size: 15px; font-weight: 300; color: var(--wine); line-height: 16px; display: block; margin-top: 2px; }
</style>
</head>
<body>
  <div class="sheet"></div>

  <svg class="band band-top" viewBox="0 0 863 15" aria-hidden="true">
    <polygon points="38,0 556,0 542,15 38,15" fill="var(--wine)"/>
    <polygon points="594,0 825,0 825,15 580,15" fill="var(--taupe)"/>
  </svg>

  <div class="abs brand-name">BRUNSMANN</div>
  <div class="abs brand-sub">Rechtsanwaltskanzlei</div>

  <div class="abs return-line">BRUNSMANN Rechtsanwaltskanzlei<span class="sep">|</span>Wiesenhang 27<span class="sep">|</span>14059 Berlin</div>

  <div class="abs contact">
    <p>Wiesenhang 27</p>
    <p>14059 Berlin</p>
    <p class="gap">Tel.&nbsp; +49-152-4 71 82 60</p>
    <p class="gap">Helga.Brunsmann@ra-brunsmann.com</p>
  </div>

  <span class="dot" style="left:112px"></span>
  <span class="dot" style="left:430px"></span>

  <div class="abs field" style="left:113px">Betreff:</div>
  <div class="abs field" style="left:338px">Aktenzeichen:</div>
  <div class="abs field" style="left:589px">Berlin, den</div>

  <span class="fold" style="top:437px"></span>
  <span class="fold" style="top:600px"></span>

  <div class="abs footer-col footer-brand" style="left:83px">
    <span class="name">BRUNSMANN</span>
    Rechtsanwaltskanzlei
  </div>
  <div class="abs footer-col" style="left:241px">
    <strong>Helga Brunsmann</strong><br>Rechtsanwältin, MBA
  </div>
  <div class="abs footer-col" style="left:399px">
    Spezialisiert auf<br><strong>Urheber- und Medienrecht</strong>
  </div>
  <div class="abs footer-col" style="left:581px">
    <strong>Hanse Kreditbank Hamburg</strong><br>BIC: HKBKDEHHXXX<br>IBAN: DE47 2105 0170 0088 3166 22
  </div>

  <svg class="band band-bottom" viewBox="0 0 863 15" aria-hidden="true">
    <polygon points="38,0 547,0 534,15 38,15" fill="var(--taupe)"/>
    <polygon points="580,0 825,0 825,15 566,15" fill="var(--wine)"/>
  </svg>
</body>
</html>
```